Bright Path Flyer Design for Virtual Online Clinic. -5.5 x 8.5 inches (half sheet)

We need a clean, modern flyer design for Bright Path, a new virtual walk-in clinic based in British Columbia. The flyer will be used in libraries, pharmacies, and community centers to help residents easily access primary care through their Bright Path NFC access card.
The flyer will ask a question : NEED A DOCTOR? This should be large and attention grabbing.
The design should clearly feature a Bright Path card image (the access card) as the centerpiece and visually show how patients can use it to book appointments. The tone should feel trustworthy, healthcare-oriented, and community-friendly — clean fonts, clear spacing, and strong readability from a distance.

Side One: This card has the NFC Access Card.
NEED A DOCTOR? (Large Font, Attention Grabbing)
How to Book an Appointment using your Bright Path Card
Step 1: Tap Your Card on Your Phone
Hold your card near the back of your phone.
It will activate automatically — no app needed.
The Bright Path scheduler will open.
Step 2: Schedule Your Appointment
Select your clinical concern.
Choose your time window.
Register (only once).
Confirm your appointment.
Step 3: Relax, we’ll take care of the rest
A doctor will call during your scheduled time.
Once booked, you’ll be able to call our office.
No emails, no texts — just a real person.
It’s that simple.
Side Two:
About Bright Path
Created by Dr. Marcus Ferrigan
Bright Path was founded to make healthcare simple and convenient. Prescription renewals. Common infections. Medical notes. And so much more.
Our doctors can address 120+ health concerns virtually — providing quality care without the waiting room. No waiting rooms. Just real doctors providing real care.
Why Patients Choose Bright Path
Easy access – book and be seen from anywhere in BC.
Effortless booking – tap your Bright Path Card to begin.
Trusted physicians – every visit is with a licensed BC family doctor.
How It Works
Book your visit — choose a time window that fits your day.
Join the queue — you’ll be called when it’s your turn.
Speak directly with your doctor — simple, secure, and stress-free.
Convenient Care for Common Concerns

Additional Details.
Please find the domain to be launched soon. I've attached the NFC card file for review, it is 85.5 mm x 54 mm. The card will be glued to the flyer.
I've attached examples of flyers but they are not the look I am seeking and I am looking for creative solutions.
Thank you!
http://brightpath-example.test/

Adult Patients in British Columbia

Healthcare

• Looking for clean lines, uniform appearance, and high legibility i.e poppins

0054AA
0677BA
7BADD7
CADEEF
E8F1F8

• Need A Doctor?
• Elegant style, not too busy, clear layout.
• Clutter, look cheap - review examples.

```html
<!DOCTYPE html>
<html lang="en">
<head>
<meta charset="utf-8">
<title>Bright Path Flyer</title>
<link rel="stylesheet" href="https://fonts.googleapis.com/css2?family=Poppins:ital,wght@0,400;0,500;0,600;0,700;0,800;1,500&family=Great+Vibes&display=swap">
<style>
:root{
  --navy:#0054AA;
  --blue:#0677BA;
  --deep:#1f3f8f;
  --sky:#7BADD7;
  --mist:#CADEEF;
  --ice:#E8F1F8;
  --green:#3ebf8c;
  --ink:#1a1a1a;
  --grey:#4a4f57;
  --stage:#5b5b5b;
}
*{box-sizing:border-box;margin:0;padding:0}
html,body{width:1200px;height:767px;overflow:hidden;background:var(--stage)}
body{position:relative;font-family:'Poppins',sans-serif;color:var(--ink)}
.page{position:absolute;top:51px;width:516px;height:668px;overflow:hidden;
  background:radial-gradient(ellipse at 50% 45%,#ffffff 0%,#f7fafd 55%,var(--ice) 100%)}
.page--front{left:56px}
.page--back{left:622px}
.brand{position:absolute;top:42px;left:0;width:100%;display:flex;justify-content:center;align-items:center;gap:8px;
  font-weight:600;font-size:27px;color:var(--deep);letter-spacing:.3px}
.brand__dot{width:12px;height:12px;border-radius:50%;background:var(--sky)}
.headline{position:absolute;top:92px;left:0;width:100%;text-align:center;font-weight:800;font-size:51px;letter-spacing:-.5px;line-height:56px;color:var(--navy)}
.headline span{color:var(--blue)}
.banner{position:absolute;left:50px;top:152px;width:415px;height:56px;border-radius:4px 4px 20px 20px;
  background:linear-gradient(90deg,var(--navy),var(--blue) 55%,var(--navy));color:#fff;text-align:center;
  font-weight:600;font-size:17px;line-height:21px;padding-top:6px}
.access-card{position:absolute;left:120px;top:229px;width:262px;height:160px;border-radius:12px;
  background:linear-gradient(90deg,var(--deep) 0%,var(--deep) 26%,#ffffff 26%,#ffffff 100%);
  border:2px solid var(--deep);box-shadow:-14px 18px 22px rgba(0,0,0,.28)}
.access-card__label{position:absolute;right:44px;bottom:17px;font-size:9px;color:var(--deep)}
.steps{position:absolute;left:0;top:418px;width:100%}
.step{position:absolute;top:0;width:146px}
.step--one{left:31px}.step--two{left:189px}.step--three{left:348px}
.step__badge{position:absolute;left:40px;top:0;width:66px;height:20px;border-radius:10px;background:var(--deep);
  color:#fff;font-weight:600;font-size:12px;text-align:center;line-height:20px}
.step__panel{position:absolute;left:0;top:52px;width:146px;height:138px;border-radius:8px;background:#fff}
.step__icon{position:absolute;left:48px;top:25px;width:50px;height:50px;border-radius:50%;background:var(--green)}
.step__title{position:absolute;top:36px;left:0;width:146px;text-align:center;font-weight:700;font-size:11.5px;line-height:14px;color:var(--ink)}
.step__list{position:absolute;top:70px;left:13px;width:122px;list-style:none;font-size:7.6px;line-height:10.5px;color:var(--grey)}
.step__list li{position:relative;padding-left:9px}
.step__list li::before{content:"✓";position:absolute;left:0;color:var(--green);font-weight:700}
.chevrons{position:absolute;top:22px}
.tagline{position:absolute;top:598px;left:0;width:100%;text-align:center;font-family:'Great Vibes',cursive;font-size:32px;color:var(--deep)}
.footer-band{position:absolute;left:50px;bottom:0;width:415px;height:14px;border-radius:14px 14px 0 0;
  background:linear-gradient(90deg,var(--navy),var(--blue),var(--navy))}
.about{position:absolute;left:37px;top:148px;width:446px;height:88px;border:1.2px solid var(--navy);border-radius:14px}
.about__title{position:absolute;left:0;top:133px;width:100%;text-align:center}
.about__title span{background:#fff;padding:0 14px;font-weight:700;font-size:23px;color:var(--navy)}
.about__by{position:absolute;top:166px;width:100%;text-align:center;font-style:italic;font-weight:500;font-size:12px;color:var(--blue)}
.about__body{position:absolute;top:182px;width:100%;text-align:center;font-size:10px;line-height:12.3px;color:var(--ink)}
.doctor-art{position:absolute;left:69px;top:253px;width:90px;height:90px;border-radius:50%;border:2px solid var(--navy);
  background:radial-gradient(circle,var(--ice),#fff)}
.reach{position:absolute;left:173px;top:257px;width:320px}
.reach__title{font-weight:700;font-size:14.5px;line-height:17px;color:var(--blue)}
.reach__body{margin-top:2px;font-size:12.6px;line-height:15px;color:var(--grey)}
.section-head{position:absolute;left:0;width:100%;display:flex;align-items:center;justify-content:center;gap:8px;font-weight:700;font-size:19px;color:var(--deep)}
.section-head::before,.section-head::after{content:"";width:50px;height:1px;background:var(--deep)}
.section-head--why{top:375px}
.section-head--how{top:477px}
.section-head em{font-style:normal;color:var(--blue)}
.feature{position:absolute;width:150px}
.feature__icon{position:absolute;left:0;top:0;width:36px;height:36px;border-radius:50%;background:var(--green)}
.feature__title{position:absolute;left:41px;top:-4px;width:125px;font-weight:600;font-size:12.5px;line-height:14px;color:var(--green)}
.feature__text{position:absolute;left:41px;width:92px;font-size:7.8px;line-height:10.5px;color:var(--ink)}
.feature--wide .feature__text{width:118px}
.closing{position:absolute;top:568px;left:0;width:100%;text-align:center;font-family:'Great Vibes',cursive;font-size:34px;color:var(--deep)}
</style>
</head>
<body>

<section class="page page--front">
  <div class="brand"><span class="brand__dot"></span>Bright Path</div>
  <h1 class="headline">NEED A <span>DOCTOR?</span></h1>
  <div class="banner">How to Book an Appointment using<br>your Bright Path Card</div>

  <div class="access-card" role="img" aria-label="Bright Path NFC access card, navy panel with white front">
    <div class="access-card__label">Tap Here to Book</div>
  </div>

  <div class="steps">
    <div class="step step--one">
      <div class="step__badge">STEP 1</div>
      <div class="step__panel">
        <div class="step__title">Tap Your Card on<br>Your Phone</div>
        <ul class="step__list">
          <li>Hold your card near the back of your phone.</li>
          <li>It will activate automatically — no app needed.</li>
          <li>The Bright Path scheduler will open.</li>
        </ul>
      </div>
      <svg class="step__icon" viewBox="0 0 50 50">
        <rect x="17" y="11" width="16" height="26" rx="3" fill="none" stroke="#fff" stroke-width="2"/>
        <line x1="22" y1="33" x2="28" y2="33" stroke="#fff" stroke-width="2"/>
      </svg>
    </div>
    <svg class="chevrons" style="left:142px" width="70" height="20" viewBox="0 0 70 20">
      <line x1="0" y1="10" x2="28" y2="10" stroke="#9bb0cc" stroke-dasharray="1.5 1.5"/>
      <g fill="none" stroke="#1f3f8f" stroke-width="3"><path d="M32 2l8 8-8 8M40 2l8 8-8 8M48 2l8 8-8 8M56 2l8 8-8 8"/></g>
    </svg>

    <div class="step step--two">
      <div class="step__badge">STEP 2</div>
      <div class="step__panel">
        <div class="step__title">Schedule Your<br>Appointment</div>
        <ul class="step__list">
          <li>Select your clinical concern.</li>
          <li>Choose your time window.</li>
          <li>Register (only once).</li>
          <li>Confirm your appointment.</li>
        </ul>
      </div>
      <svg class="step__icon" viewBox="0 0 50 50">
        <rect x="13" y="14" width="24" height="22" rx="2" fill="none" stroke="#fff" stroke-width="2"/>
        <line x1="13" y1="20" x2="37" y2="20" stroke="#fff" stroke-width="2"/>
        <line x1="19" y1="11" x2="19" y2="16" stroke="#fff" stroke-width="2"/>
        <line x1="31" y1="11" x2="31" y2="16" stroke="#fff" stroke-width="2"/>
      </svg>
    </div>
    <svg class="chevrons" style="left:305px" width="70" height="20" viewBox="0 0 70 20">
      <line x1="0" y1="10" x2="28" y2="10" stroke="#9bb0cc" stroke-dasharray="1.5 1.5"/>
      <g fill="none" stroke="#1f3f8f" stroke-width="3"><path d="M32 2l8 8-8 8M40 2l8 8-8 8M48 2l8 8-8 8M56 2l8 8-8 8"/></g>
    </svg>

    <div class="step step--three">
      <div class="step__badge">STEP 3</div>
      <div class="step__panel">
        <div class="step__title">Relax, we’ll take<br>care of the rest</div>
        <ul class="step__list">
          <li>A doctor will call during your scheduled time.</li>
          <li>Once booked, you’ll be able to call our office.</li>
          <li>No emails, no texts — just a real person.</li>
        </ul>
      </div>
      <svg class="step__icon" viewBox="0 0 50 50">
        <circle cx="25" cy="25" r="14" fill="none" stroke="#fff" stroke-width="2"/>
        <path d="M18 25l5 5 9-10" fill="none" stroke="#fff" stroke-width="2.4"/>
      </svg>
    </div>
  </div>

  <div class="tagline">it’s that Simple</div>
  <div class="footer-band"></div>
</section>

<section class="page page--back">
  <div class="brand"><span class="brand__dot"></span>Bright Path</div>

  <div class="about"></div>
  <h2 class="about__title"><span>About Bright Path</span></h2>
  <p class="about__by">Created by Dr. Marcus Ferrigan</p>
  <p class="about__body">Bright Path was founded to make healthcare simple and convenient.<br>Prescription renewals. Common infections. Medical notes.<br>And so much more.</p>

  <div class="doctor-art" role="img" aria-label="Virtual doctor consultation on a screen"></div>
  <div class="reach">
    <p class="reach__title">Our doctors can address 120+ health concerns virtually</p>
    <p class="reach__body">providing quality care without the waiting room. No waiting rooms. Just real doctors providing real care.</p>
  </div>

  <h2 class="section-head section-head--why"><span>Why Patients <em>Choose Bright Path</em></span></h2>

  <div class="feature" style="left:35px;top:422px">
    <svg class="feature__icon" viewBox="0 0 36 36"><rect x="10" y="10" width="16" height="15" rx="2" fill="none" stroke="#fff" stroke-width="1.6"/><line x1="10" y1="15" x2="26" y2="15" stroke="#fff" stroke-width="1.6"/></svg>
    <div class="feature__title">Easy access</div>
    <p class="feature__text" style="top:12px">Book and be seen from anywhere in BC.</p>
  </div>
  <div class="feature" style="left:173px;top:424px">
    <svg class="feature__icon" viewBox="0 0 36 36"><rect x="8" y="11" width="20" height="10" rx="2" fill="none" stroke="#fff" stroke-width="1.6"/><path d="M17 18v9" stroke="#fff" stroke-width="1.6"/></svg>
    <div class="feature__title">Effortless booking</div>
    <p class="feature__text" style="top:12px">Tap your Bright Path Card to begin.</p>
  </div>
  <div class="feature feature--wide" style="left:331px;top:422px">
    <svg class="feature__icon" viewBox="0 0 36 36"><circle cx="18" cy="18" r="9" fill="none" stroke="#fff" stroke-width="1.6"/><path d="M14 18l3 3 5-6" fill="none" stroke="#fff" stroke-width="1.6"/></svg>
    <div class="feature__title">Trusted physicians</div>
    <p class="feature__text" style="top:12px">Every visit is with a licensed BC family doctor.</p>
  </div>

  <h2 class="section-head section-head--how"><span>How It <em>Works</em></span></h2>

  <div class="feature" style="left:35px;top:516px">
    <svg class="feature__icon" viewBox="0 0 36 36"><path d="M10 18l6 6 10-12" fill="none" stroke="#fff" stroke-width="2.6"/></svg>
    <div class="feature__title">Book your visit</div>
    <p class="feature__text" style="top:14px">choose a time window that fits your day.</p>
  </div>
  <div class="feature" style="left:173px;top:518px">
    <svg class="feature__icon" viewBox="0 0 36 36"><path d="M10 18l6 6 10-12" fill="none" stroke="#fff" stroke-width="2.6"/></svg>
    <div class="feature__title">Join the queue</div>
    <p class="feature__text" style="top:14px">you’ll be called when it’s your turn.</p>
  </div>
  <div class="feature feature--wide" style="left:331px;top:516px">
    <svg class="feature__icon" viewBox="0 0 36 36"><path d="M10 18l6 6 10-12" fill="none" stroke="#fff" stroke-width="2.6"/></svg>
    <div class="feature__title">Speak directly with your doctor</div>
    <p class="feature__text" style="top:28px">simple, secure, and stress-free.</p>
  </div>

  <div class="closing">Convenient Care for Common Concerns</div>
  <div class="footer-band"></div>
</section>

</body>
</html>
```